Flyer for the Lumen 2025 Conference

I am looking to produce a flyer for our upcoming conference, Lumen 2025. This is an annual conference that we plan to publicize on social media. The ideal designer will create a flyer that is eye-catching and effectively communicates the key information. Please see attached our logo, speaker photo, and flyer content.

Target Market(s)

All demographics

Industry/Entity Type

Christian

Font styles to use
Sans Serif

Requirements
Should not have
• Cross, church

```html
<!DOCTYPE html>
<html lang="en">
<head>
<meta charset="utf-8">
<title>Lumen 2025 Conference</title>
<link href="https://fonts.googleapis.com/css2?family=Roboto:wght@300;400;500;700;900&family=Roboto+Condensed:wght@700&display=swap" rel="stylesheet">
<style>
  :root{
    --ember-dark:#2a0702;
    --ember:#b8330a;
    --ember-bright:#f2641c;
    --blue:#0a86d4;
    --blue-deep:#0b5fa8;
    --orange:#f7941d;
    --white:#ffffff;
    --ink:#1c1c1c;
  }
  *{margin:0;padding:0;box-sizing:border-box}
  html,body{width:846px;height:1200px;overflow:hidden;background:var(--ember-dark)}
  .flyer{
    position:relative;width:846px;height:1200px;overflow:hidden;
    font-family:'Roboto',sans-serif;color:var(--white);
    background:
      radial-gradient(ellipse 60% 45% at 55% 30%, var(--ember-bright) 0%, var(--ember) 45%, transparent 80%),
      radial-gradient(ellipse 50% 40% at 80% 80%, #3a3a3a 0%, transparent 70%),
      linear-gradient(160deg, #7a1d05 0%, var(--ember) 35%, #5a1204 65%, #151515 100%);
  }
  .halo{position:absolute;left:58px;top:20px;width:730px;height:730px;border-radius:50%;background:rgba(255,140,60,.12)}
  .brand{position:absolute;left:186px;top:46px;display:flex;align-items:center;gap:8px}
  .brand-dot{width:18px;height:18px;border-radius:50%;background:var(--orange)}
  .brand-name{font-size:46px;font-weight:400;letter-spacing:2px;color:var(--white)}
  .brand-line{position:absolute;left:198px;top:128px;font-size:11px;letter-spacing:1px;color:var(--orange)}
  .title{position:absolute;left:0;width:846px;text-align:center;font-weight:900;line-height:1}
  .title-word{top:165px;font-size:160px;letter-spacing:-2px;padding-left:40px}
  .title-year{top:292px;font-size:210px;font-weight:500;letter-spacing:22px;padding-left:60px}
  .photo{position:absolute;left:0;top:420px;width:510px;height:780px;
    background:linear-gradient(180deg, rgba(40,20,15,0) 0%, rgba(24,86,170,.85) 35%, #0d63b8 70%, #0a3f7a 100%);
    border-top-left-radius:40% 20%;border-top-right-radius:40% 20%}
  .subtitle{position:absolute;left:232px;top:484px;font-size:31px;letter-spacing:1px}
  .subtitle b{font-weight:900}
  .subtitle span{font-weight:300;letter-spacing:2px}
  .topic-label{position:absolute;left:231px;top:533px;font-size:20px}
  .topic-band{position:absolute;left:198px;top:561px;width:590px;height:46px;background:var(--blue)}
  .topic-text{position:absolute;left:232px;top:563px;font-family:'Roboto Condensed',sans-serif;font-weight:700;font-size:38px;letter-spacing:1px}
  .day{position:absolute;top:640px;width:169px;height:158px;border:3px solid var(--blue);text-align:center}
  .day-month{margin-top:10px;font-weight:700;font-size:22px;letter-spacing:1px;color:var(--blue)}
  .day-date{font-family:'Roboto Condensed',sans-serif;font-weight:700;font-size:56px;line-height:1}
  .day-date span{font-family:'Roboto',sans-serif;font-weight:300}
  .day-name{font-weight:700;font-size:21px;letter-spacing:1px;color:var(--orange);margin-top:2px}
  .day-time{position:absolute;left:14px;top:119px;width:135px;height:70px;background:var(--blue);
    color:var(--blue-deep);font-weight:700;font-size:22px;line-height:22px;padding-top:12px}
  .day-time{color:#0c4f8f}
  .venue{position:absolute;right:266px;top:854px;text-align:right;line-height:1.15}
  .venue-name{font-weight:700;font-size:23px;color:var(--orange);letter-spacing:.5px}
  .venue-sub{font-size:17px;letter-spacing:1px}
  .venue-addr{font-size:21px;margin-top:4px}
  .pin{position:absolute;left:590px;top:858px}
  .contact{position:absolute;left:578px;top:968px;font-size:21px;line-height:25px}
  .contact div{display:flex;align-items:center;gap:10px}
  .contact .phone{font-weight:700;font-size:24px}
  .contact .web{color:var(--orange)}
  .contact svg{width:18px;height:18px;flex:none}
  .app{position:absolute;left:605px;top:1070px;font-size:13px;line-height:1.2}
  .app b{font-weight:700;font-size:19px;color:var(--orange)}
  .badge{position:absolute;top:1132px;width:83px;height:26px;border-radius:4px;background:var(--white)}
  .speaker-label{position:absolute;left:289px;top:1090px;font-size:21px}
  .speaker-label b{font-weight:700}
  .speaker-name{position:absolute;left:288px;top:1118px;font-family:'Roboto Condensed',sans-serif;font-weight:700;font-size:44px;letter-spacing:1px;color:var(--orange)}
</style>
</head>
<body>
<main class="flyer">
  <div class="halo"></div>

  <div class="brand"><span class="brand-dot"></span><span class="brand-name">VERAN</span></div>
  <div class="brand-line">A LIGHT TO EVERY SHORE</div>

  <h1 class="title title-word">LUMEN</h1>
  <div class="title title-year">2025</div>

  <div class="photo" role="img" aria-label="Portrait of the speaker in a blue suit, seated"></div>

  <p class="subtitle"><b>A PROPHETIC</b> <span>CONFERENCE</span></p>
  <p class="topic-label">Topic:</p>
  <div class="topic-band"></div>
  <h2 class="topic-text">THE VOICE OF THE LORD</h2>

  <section class="day" style="left:234px">
    <div class="day-month">DECEMBER</div>
    <div class="day-date">26<span>TH</span></div>
    <div class="day-name">FRIDAY</div>
    <div class="day-time">6:30 PM<br>9:00 PM</div>
  </section>
  <section class="day" style="left:427px">
    <div class="day-month">DECEMBER</div>
    <div class="day-date">27<span>TH</span></div>
    <div class="day-name">SATURDAY</div>
    <div class="day-time">5:30 PM<br>8:00 PM</div>
  </section>
  <section class="day" style="left:620px">
    <div class="day-month">DECEMBER</div>
    <div class="day-date">28<span>TH</span></div>
    <div class="day-name">SUNDAY</div>
    <div class="day-time">4:30 PM<br>7:00 PM</div>
  </section>

  <address class="venue" style="font-style:normal">
    <div class="venue-name">THE ASHFORD</div>
    <div class="venue-sub">PERFORMING ARTS CENTER</div>
    <div class="venue-addr">218 Millbrook Avenue<br>Ashford, Maine 04010</div>
  </address>
  <svg class="pin" width="16" height="22" viewBox="0 0 16 22"><path d="M8 0a8 8 0 0 0-8 8c0 6 8 14 8 14s8-8 8-14a8 8 0 0 0-8-8z" fill="#f7941d"/><circle cx="8" cy="8" r="3" fill="#3a1205"/></svg>

  <div class="contact">
    <div class="phone"><svg viewBox="0 0 24 24"><path d="M6.6 10.8a15 15 0 0 0 6.6 6.6l2.2-2.2a1 1 0 0 1 1-.25 11 11 0 0 0 3.6.6 1 1 0 0 1 1 1V20a1 1 0 0 1-1 1A17 17 0 0 1 3 4a1 1 0 0 1 1-1h3.5a1 1 0 0 1 1 1 11 11 0 0 0 .6 3.6 1 1 0 0 1-.25 1z" fill="#f7941d"/></svg>207 555 0142</div>
    <div><svg viewBox="0 0 24 24"><rect x="2" y="5" width="20" height="14" fill="#f7941d"/><path d="M2 5l10 8 10-8" stroke="#2a0702" stroke-width="2" fill="none"/></svg>hello@veran.org</div>
    <div class="web"><svg viewBox="0 0 24 24"><circle cx="12" cy="12" r="9" fill="none" stroke="#f7941d" stroke-width="2"/><path d="M3 12h18M12 3c4 4 4 14 0 18M12 3c-4 4-4 14 0 18" stroke="#f7941d" stroke-width="1.5" fill="none"/></svg>www.veran.org</div>
  </div>

  <div class="app">Download the<br><b>VERAN</b> <span style="font-size:17px">App</span><br>to stay updated on the event</div>
  <div class="badge" style="left:605px"></div>
  <div class="badge" style="left:699px"></div>

  <p class="speaker-label">Speaker:&nbsp; <b>Prophet</b></p>
  <p class="speaker-name">ELIAS NARVO</p>
</main>
</body>
</html>
```